Business Card & Logo Design - Hedge Fund

We need a business card and logo design for a hedge fund. The hedge fund is named Morvane Equity LLC. Morvane Equity was created by finance professors and the strategy is based academic research that looks for patterns in stock prices. The design should look conservative, solid, strong. We favor a classic style - nothing flashy. The logo can relate to the name Morvane Equity, or it could involve a symbol design that connotes "science" . We are open to ideas. We do not want alot of colors - but if any, color - blue is preferred. The font that seems to look best for the name (Morvane Equity) is arial black. We are open to ideas. Most important - we want to see a mock up of an actual business card with the logo concept embedded. The business card should include space for : company name, individual name, position title, cell phone, address. We hope to have this work done by Sept. 8.

Target Market(s)

We will be meeting with and giving the business card to institutions and high net worth individuals.

Industry/Entity Type

Investment Advisory

Contact Information for Business Card

Company name - Morvane Equity LLC
Individual name - Peter Dalby
Title - Portfolio Manager
Cell - (412) 555-0187
Address - 2650 Birchmont Lane, Suite 300, Atlanta GA 30327

Font styles to use
Other font styles liked:
• Arial

Colors
3277b5
0255a3
85acd3
cedeed
fdf9cf
d9d9d9
e6e6e6
f04a50
6b449b

Requirements
Must have
• Must have card details that are sited above.
• We would like a logo related to the name (Morvane Equity) or concept of the fund.
Nice to have
• We want conservative / understated / clean crisp look.
• If any colors - we prefer conservative appearance - blue / gray.
• I have enclosed an example of a card style that looks attractive - please do not exactly copy this card. This is not our company or logo. I feel the layout is attractive - just as an example
Should not have
• Avoid too much color.
• I have selected some preferred colors. Please do not use all of the colors - I have selected a few that might work - but I am not sure. We are open to your ideas so please do not feel the need to use all or any of these.

```html
<!DOCTYPE html>
<html lang="en">
<head>
<meta charset="utf-8">
<title>Morvane Equity LLC – Business Card</title>
<link rel="stylesheet" href="https://fonts.googleapis.com/css2?family=Arimo:wght@400;700&display=swap">
<style>
  :root {
    --navy: #003f7f;
    --band: #004183;
    --title-blue: #5a84b0;
    --ring-grey: #cbcbcb;
    --edge-grey: #bdbdbd;
    --paper: #ffffff;
  }
  html, body {
    margin: 0;
    padding: 0;
    width: 1200px;
    height: 735px;
    overflow: hidden;
    background: var(--paper);
  }
  .card {
    position: relative;
    width: 1200px;
    height: 735px;
    box-sizing: border-box;
    border: 2px solid var(--edge-grey);
    background: var(--paper);
    font-family: "Arimo", Arial, sans-serif;
    color: var(--navy);
    overflow: hidden;
  }
  .brand-mark {
    position: absolute;
    left: 242px;
    top: 243px;
    width: 150px;
    height: 150px;
    border-radius: 50%;
    box-sizing: border-box;
    border: 8px solid var(--ring-grey);
    background: var(--paper);
    box-shadow: 0 0 28px 10px rgba(0, 0, 0, 0.06);
  }
  .brand-name {
    position: absolute;
    left: 82px;
    top: 398px;
    margin: 0;
    font-size: 50px;
    font-weight: 400;
    line-height: 1;
    white-space: nowrap;
  }
  .person {
    position: absolute;
    left: 721px;
    top: 160px;
  }
  .person-name {
    margin: 0;
    font-size: 36px;
    font-weight: 700;
    line-height: 1.05;
  }
  .person-title {
    margin: 0;
    font-size: 36px;
    font-weight: 400;
    line-height: 1.05;
    color: var(--title-blue);
  }
  .contact {
    position: absolute;
    left: 720px;
    display: flex;
    align-items: flex-start;
    font-size: 30px;
    line-height: 38px;
  }
  .contact svg {
    flex: none;
    margin-right: 8px;
  }
  .contact-address { top: 380px; }
  .contact-address svg { margin-top: 6px; }
  .contact-phone { top: 533px; }
  .contact-phone svg { margin-top: 3px; }
  .footer-band {
    position: absolute;
    left: 0;
    right: 0;
    bottom: 0;
    height: 121px;
    background: var(--band);
  }
</style>
</head>
<body>
  <div class="card">
    <div class="brand-mark" aria-hidden="true"></div>
    <h1 class="brand-name">Morvane Equity LLC</h1>

    <div class="person">
      <p class="person-name">Peter Dalby</p>
      <p class="person-title">Portfolio Manager</p>
    </div>

    <div class="contact contact-address">
      <svg width="20" height="28" viewBox="0 0 20 28" aria-hidden="true">
        <path d="M10 1C5 1 1.5 4.7 1.5 9.4 1.5 15.6 10 27 10 27s8.5-11.4 8.5-17.6C18.5 4.7 15 1 10 1z" fill="var(--navy)"/>
        <circle cx="10" cy="9.5" r="3.4" fill="var(--paper)"/>
      </svg>
      <span>2650 Birchmont Lane,<br>Suite 300, Atlanta GA<br>30327</span>
    </div>

    <div class="contact contact-phone">
      <svg width="22" height="34" viewBox="0 0 22 34" aria-hidden="true">
        <rect x="2" y="2" width="18" height="30" rx="3" fill="none" stroke="var(--navy)" stroke-width="2.4"/>
        <circle cx="11" cy="27" r="1.6" fill="var(--navy)"/>
      </svg>
      <span>(412) 555-0187</span>
    </div>

    <div class="footer-band"></div>
  </div>
</body>
</html>
```